Boutique personal training and fitness studio - banner ad design

We need a 'revolving' banner ad designed for our personal training and fitness studio. There are three separate offers (i.e. 3 pages to the advertisements)
Offer 1
PT Starter Pack
3 personal training sessions
$119
New clients only
Offer 2
Group fitness
2 weeks unlimited group fitness classes
$29
New clients only
Offer 3
Strength starter pack
2 weeks unlimited group fitness classes and 2 PT sessions
$89
New clients only
Please do not put the words "Offer 1, 2 or 3" in the ads - just the text following each offer.
Each advertisement should be sized to fit across around half of the webpage and be in landscape format.
Each advertisement should have a suitable picture (no cartoons) and should be complimentary to the existing website.
Each advertisement should also include the logo (attached)
www.harrowdaleliftroom.com.au
Training

```html
<!DOCTYPE html>
<html lang="en">
<head>
<meta charset="utf-8">
<title>Harrowdale Lift Room – Starter Offers</title>
<link rel="stylesheet" href="https://fonts.googleapis.com/css2?family=Arimo:wght@400;700&display=swap">
<style>
  :root {
    --page: #ffffff;
    --ink-dark: #000000;
    --ink-white: #f2f2f2;
    --pt-red: #f0222a;
    --pt-tan: #d4995a;
    --group-bg: #efedeb;
    --group-band: #7b6a5e;
    --group-title: #333333;
    --group-blue: #2aa6ee;
    --group-brown: #7b6858;
    --strength-yellow: #e1dc86;
    --strength-green: #7cb84a;
    --strength-mint: #a8e6c8;
    --badge-bg: #111111;
    --badge-text: #e6e6e6;
  }
  html, body { margin: 0; padding: 0; overflow: hidden; }
  body { background: var(--page); font-family: "Arimo", Arial, sans-serif; }
  .canvas { position: relative; width: 750px; height: 1200px; overflow: hidden; background: var(--page); }
  .banner { position: absolute; left: 46px; width: 666px; height: 331px; overflow: hidden; }
  .banner > * { position: absolute; margin: 0; }
  .title { font-weight: 700; font-size: 55px; line-height: 1; white-space: nowrap; }
  .count { font-weight: 700; font-size: 112px; line-height: 1; }
  .detail { font-weight: 700; font-size: 30px; line-height: 1.22; }
  .price { font-weight: 700; font-size: 56px; line-height: 1; letter-spacing: -1px; }
  .terms { font-weight: 700; font-size: 20px; line-height: 1; white-space: nowrap; }
  .brand-badge {
    display: flex; align-items: center; justify-content: center; text-align: center;
    background: var(--badge-bg); color: var(--badge-text);
    font-weight: 700; font-size: 13px; line-height: 1.1; text-transform: uppercase; letter-spacing: 0.5px;
  }
  .photo { }

  /* PT starter pack */
  .pt-offer { top: 60px; background: var(--ink-dark); }
  .pt-offer .photo { right: 0; top: 0; width: 260px; height: 331px;
    background: radial-gradient(ellipse at 55% 45%, #5a4a40 0%, #2c2420 45%, #000 80%); }
  .pt-offer .title { left: 16px; top: 22px; color: var(--ink-white); }
  .pt-offer .count { left: 86px; top: 110px; color: var(--pt-red); }
  .pt-offer .detail { left: 181px; top: 118px; color: var(--pt-tan); }
  .pt-offer .price { left: 31px; top: 234px; color: var(--ink-white); }
  .pt-offer .terms { left: 31px; top: 290px; color: var(--ink-white); }
  .pt-offer .brand-badge { left: 229px; top: 246px; width: 128px; height: 56px; }

  /* Group fitness */
  .group-offer { top: 421px; background: var(--group-bg); }
  .group-offer .band { left: 0; top: 219px; width: 666px; height: 112px; background: var(--group-band); }
  .group-offer .photo { left: 0; top: 0; width: 156px; height: 331px;
    background: linear-gradient(180deg, #e2d4c6 0%, #c9a88e 40%, #4a4a52 70%, #9a9aa0 100%); }
  .group-offer .title { left: 210px; top: 14px; color: var(--group-title); }
  .group-offer .count { left: 208px; top: 104px; color: var(--group-blue); }
  .group-offer .detail { left: 294px; top: 100px; color: var(--group-brown); }
  .group-offer .brand-badge { left: 210px; top: 251px; width: 128px; height: 58px; }
  .group-offer .price { right: 58px; top: 240px; color: var(--ink-dark); }
  .group-offer .terms { right: 28px; top: 296px; color: var(--ink-dark); }

  /* Strength starter pack */
  .strength-offer { top: 780px; background: var(--ink-dark); }
  .strength-offer .photo { left: 90px; top: 72px; width: 420px; height: 160px;
    background: radial-gradient(ellipse at 50% 40%, #8a8a8a 0%, #3a3a3a 35%, #000 75%); }
  .strength-offer .title { left: 0; width: 666px; text-align: center; top: 14px; font-size: 57px; color: var(--strength-yellow); }
  .strength-offer .count { left: 20px; top: 212px; color: var(--strength-green); }
  .strength-offer .detail { left: 108px; top: 218px; color: var(--strength-mint); }
  .strength-offer .price { left: 516px; top: 168px; color: var(--ink-white); }
  .strength-offer .terms { left: 502px; top: 224px; color: var(--ink-white); }
  .strength-offer .brand-badge { left: 522px; top: 260px; width: 122px; height: 57px; }
</style>
</head>
<body>
<main class="canvas">

  <section class="banner pt-offer">
    <div class="photo" role="img" aria-label="Muscular man's bare torso in low light"></div>
    <h2 class="title">PT Starter Pack</h2>
    <span class="count">3</span>
    <p class="detail">personal training<br>sessions</p>
    <p class="price">$119</p>
    <p class="terms">New clients only</p>
    <div class="brand-badge">Harrowdale<br>Lift Room</div>
  </section>

  <section class="banner group-offer">
    <div class="band"></div>
    <div class="photo" role="img" aria-label="Woman in sports top lifting a dumbbell"></div>
    <h2 class="title">Grpoup fitness</h2>
    <span class="count">2</span>
    <p class="detail">weeks unlimited<br>group fitness<br>classes</p>
    <div class="brand-badge">Harrowdale<br>Lift Room</div>
    <p class="price">$29</p>
    <p class="terms">New clients only</p>
  </section>

  <section class="banner strength-offer">
    <div class="photo" role="img" aria-label="Athlete seen from behind with arms spread wide"></div>
    <h2 class="title">Strength starter pack</h2>
    <span class="count">2</span>
    <p class="detail">weeks unlimited<br>group fitness classes<br>and 2 PT sessions</p>
    <p class="price">$89</p>
    <p class="terms">New clients only</p>
    <div class="brand-badge">Harrowdale<br>Lift Room</div>
  </section>

</main>
</body>
</html>
```